A Business Card and Letterhead for a Surgeon in Practice

Design a Business Card and Business Letterhead with theming consistent with my website, logo and referral pad which will be uploaded for reference.

Website found at: www.bertramholvey.com.au

A text file is uploaded indicating what information needs to be on the business card and a separate document for the letterhead.

The other images I have uploaded are entirely optional for artistic design. None of them necessarily have to be used. Further imagery may or may not be included as per the designer to get the best result
Updates

Industry/Entity Type

Medical

Requirements
Must have
• Logo as uploaded. Certain text as uploaded.
• NEW as of 8th August:
• **On the back there needs to be a blank space incorporating at least half of the vertical distance of the card - this is where stickers can be placed in the office for certain appointment details**
• **Also, for the consulting locations a small box next to each should be included so that it can be ticked by my secretary indicating the correct location**

```html
<!DOCTYPE html>
<html lang="en">
<head>
<meta charset="utf-8">
<title>Bertram Holvey – Business Card</title>
<link rel="stylesheet" href="https://fonts.googleapis.com/css2?family=Arimo:wght@400;700&family=Cinzel:wght@400;600&display=swap">
<style>
  :root {
    --backdrop: #3f3632;
    --card: #1d1d1e;
    --sticker: #262627;
    --rule: #4a4a4c;
    --teal: #1f9c92;
    --white: #f2f2f2;
    --grey: #9a9a9a;
    --photo-light: #d9d9d9;
    --photo-dark: #5a5f66;
  }
  * { box-sizing: border-box; margin: 0; padding: 0; }
  html, body { width: 1200px; height: 787px; overflow: hidden; }
  body {
    background: var(--backdrop);
    font-family: "Arimo", Arial, sans-serif;
    color: var(--white);
    position: relative;
  }
  .card {
    position: absolute;
    top: 235px;
    width: 520px;
    height: 317px;
    background: var(--card);
    border-radius: 4px;
    box-shadow: 0 10px 26px rgba(0,0,0,.45);
    overflow: hidden;
  }
  .card--back { left: 45px; }
  .card--front { left: 635px; }

  .brand-mark {
    position: absolute;
    display: flex;
    align-items: center;
    gap: 10px;
    white-space: nowrap;
  }
  .brand-mark .dot {
    border-radius: 50%;
    background: var(--teal);
    flex: none;
  }
  .brand-mark .name {
    font-family: "Cinzel", "Times New Roman", serif;
    font-weight: 600;
    color: var(--teal);
    letter-spacing: 1px;
    line-height: 1;
  }

  /* back */
  .card--back .brand-mark {
    top: 16px; left: 50%;
    transform: translateX(-50%);
    gap: 8px;
  }
  .card--back .brand-mark .dot { width: 14px; height: 14px; }
  .card--back .brand-mark .name { font-size: 20px; }
  .locations-title {
    position: absolute;
    top: 44px; left: 0; right: 0;
    text-align: center;
    font-family: "Cinzel", "Times New Roman", serif;
    font-weight: 400;
    font-size: 16px;
    color: var(--teal);
    letter-spacing: 1px;
  }
  .locations {
    position: absolute;
    top: 68px; left: 34px; right: 30px;
    list-style: none;
    font-size: 12.5px;
    line-height: 19px;
  }
  .locations li { display: flex; align-items: center; gap: 8px; white-space: nowrap; }
  .tick-box {
    width: 10px; height: 10px; flex: none;
    border: 1px solid var(--teal);
    border-radius: 1px;
  }
  .locations .label { color: var(--teal); font-weight: 700; }
  .sticker-space {
    position: absolute;
    left: 14px; right: 14px;
    top: 150px; bottom: 8px;
    background: var(--sticker);
    border: 1px dashed var(--rule);
    border-radius: 4px;
  }

  /* front */
  .card--front .brand-mark { top: 34px; left: 40px; align-items: flex-start; }
  .card--front .brand-mark .dot { width: 30px; height: 30px; margin-top: 2px; }
  .card--front .brand-mark .name { font-size: 27px; }
  .specialty {
    display: block;
    font-family: "Cinzel", "Times New Roman", serif;
    font-size: 9.5px;
    letter-spacing: 1.2px;
    color: var(--grey);
    margin-top: 6px;
  }
  .contacts {
    position: absolute;
    top: 118px; left: 40px;
    list-style: none;
    font-size: 15.5px;
    line-height: 23px;
  }
  .contacts li { display: flex; align-items: center; gap: 9px; }
  .contacts svg { width: 14px; height: 14px; flex: none; }
  .portrait {
    position: absolute;
    right: 30px; bottom: 24px;
    width: 150px; height: 168px;
    border-radius: 12px;
    background: linear-gradient(180deg, var(--photo-light) 0%, var(--photo-light) 55%, var(--photo-dark) 100%);
  }
</style>
</head>
<body>

<section class="card card--back" aria-label="Card back">
  <div class="brand-mark">
    <span class="dot"></span>
    <span class="name">Bertram Holvey</span>
  </div>
  <h2 class="locations-title">CONSULTING LOCATIONS</h2>
  <ul class="locations">
    <li><span class="tick-box"></span><span><span class="label">Melbourne :</span> Carrick St CBD, Box Hill, Rowville</span></li>
    <li><span class="tick-box"></span><span><span class="label">Regional :</span> Bendigo, Kyneton, Latrobe Valley</span></li>
    <li><span class="tick-box"></span><span><span class="label">Operating locations :</span> Eastgate Private Hospital</span></li>
    <li><span class="tick-box"></span><span>Riverside Hospital, Hillcrest Hospital, Southvale Hospital</span></li>
  </ul>
  <div class="sticker-space" aria-label="Blank space for appointment sticker"></div>
</section>

<section class="card card--front" aria-label="Card front">
  <div class="brand-mark">
    <span class="dot"></span>
    <div>
      <span class="name">Bertram Holvey</span>
      <span class="specialty">General, Upper GI &amp; Bariatric Surgeon</span>
    </div>
  </div>

  <ul class="contacts">
    <li>
      <svg viewBox="0 0 14 14" aria-hidden="true"><path fill="var(--teal)" d="M3 1h2.5l1 3-1.5 1.2a7 7 0 0 0 3.8 3.8L10 7.5l3 1V11a2 2 0 0 1-2 2A10 10 0 0 1 1 3a2 2 0 0 1 2-2z"/></svg>
      03 9000 4821
    </li>
    <li>
      <svg viewBox="0 0 14 14" aria-hidden="true"><rect x="2" y="2" width="10" height="10" rx="1.5" fill="var(--teal)"/><rect x="4" y="4" width="6" height="4" fill="var(--card)"/></svg>
      03 9000 4839
    </li>
    <li>
      <svg viewBox="0 0 14 14" aria-hidden="true"><rect x="4" y="1" width="6" height="12" rx="1.2" fill="var(--teal)"/><rect x="5" y="2.5" width="4" height="7" fill="var(--card)"/></svg>
      0400 118 276
    </li>
    <li>
      <svg viewBox="0 0 14 14" aria-hidden="true"><rect x="1" y="3" width="12" height="8" rx="1" fill="var(--teal)"/><path d="M1.5 3.5 7 8l5.5-4.5" stroke="var(--card)" stroke-width="1.2" fill="none"/></svg>
      info@southbankweightsurgery.com.au
    </li>
    <li>
      <svg viewBox="0 0 14 14" aria-hidden="true"><circle cx="7" cy="7" r="5.5" fill="none" stroke="var(--teal)" stroke-width="1.4"/><path d="M1.5 7h11M7 1.5c-2.5 3-2.5 8 0 11M7 1.5c2.5 3 2.5 8 0 11" stroke="var(--teal)" stroke-width="1" fill="none"/></svg>
      bertramholvey.com.au
    </li>
    <li>
      <svg viewBox="0 0 14 14" aria-hidden="true"><rect x="1.5" y="1.5" width="11" height="11" rx="1.5" fill="var(--teal)"/></svg>
      groups/bertramholvey
    </li>
  </ul>

  <div class="portrait" role="img" aria-label="Portrait photograph of the surgeon in a suit"></div>
</section>

</body>
</html>
```